Book Cover for a book on Lantern Road Ventures

I am self-publishing my book on Brindlemark and need a book cover made. Below are the details. See attached templates for size we need to use. I also attached a previous cover we had made that I liked. The problem with it was they were two boys helping each other but the book is about women. I'm open to your ideas on the cover though, but I wanted to show you a style I liked as an idea.
Front of Cover
Book Title: Lantern Road Ventures
Book Subtitle: Loose Pages of a Harbor Keeper
Author Name: Mirela T. Dunbar
Add on the Spine of Cover: Lantern Road Ventures and Mirela T. Dunbar
Back of the Cover Text:
Lantern Road Ventures: Loose Pages of a Harbor Keeper is an honest account of a business owner’s experience attempting to navigate the start-up community while also pursuing spiritual growth. Author Mirela Dunbar defines a spiritual entrepreneur as “someone who runs an enterprise with the purpose of growing love rather than material gain.” This book discusses the three dimensions of Lantern Road Ventures:
1. The business is an integral part of the founder’s spiritual journey.
2. Employees working for the spiritual enterprise, whether they know it or not, encounter this company because it's part of their spiritual path.
3. The business itself has a life force of its own and its purpose is to further the kingdom of heaven on earth.
These three dimensions happen simultaneously and work together to produce the greatest possible result. However, this can feel confusing to a founder juggling these dimensions while also trying to manage and run a business. This is not a formulaic self-help book or roadmap. Rather, it is a compilation of personal reflections that often seem at odds with the traditional world of entrepreneurship.
Below the description add my picture (see attached for my picture)
Bio text:
Mirela Dunbar founded Calveta with the vision of ushering in a life-long education system that shifts away from standardization to one that empowers people to live their purpose. In college, Mirela interned for Open Kettle, a women’s empowerment initiative where she recognized her passion for helping people find their voice. Mirela's 20-year journey has come full circle to empowering other female CEOs who are pursuing the path of Lantern Road Ventures.
NOTE: Please note that Brindlemark puts a bar code on the bottom right of the back cover as is noted on the attached template.
Size template is attached to the brief, here are the sizes typed out:
# Description Width (in) Height (in)
1 Full Cover 12.79 9.25
2 Front Cover 6 9
3 Safe Area 5.875 8.75
4 Bleed 0.125 0.125
5 Margin 0.125 0.125
6 Spine 0.54 9
7 Spine Safe Area 0.415 8.75
8 Spine Margin 0.062 0.062
9 Barcode Margin 0.25 0.25
Pre-publication checklist
BRINDLEMARK TIPS for the final cover:
1. Save as a PDF. Your cover must be a single PDF that includes the back cover, spine, and front cover as one image.
2. Flatten all transparencies. These can cause the file to print with missing or distorted content. Consult your software's documentation to learn how.
3. Embed your fonts. Consult your software's documentation to learn how.
4. Remove crop marks, color bars, template text. Crop marks are lines showing where pages should be trimmed. Color bars are strips with a series of patches used to ensure color balance during printing. Also, remove any template text, PDF creation guides, or software references.
5. Ensure your cover image meets the minimum resolution of 300 DPI (dots per inch).
6. Optimize PDFs. Optimization is useful to reduce your file size, allowing for higher performance when transferring, uploading, viewing, and printing the files.
7. Remove file security. Locked or encrypted files will fail review.
Target Market(s)
Women who want to be CEOs or are currently CEOs of companies.
Industry/Entity Type
Entrepreneurship, business, spirituality
Requirements
Must have
- Just the text on the description. A very welcoming feel.
Nice to have
- I like the idea of having a sunrise/sunset in the image somehow like in the example I attached to the brief, but again I'm open.
Should not have
- Please don't put any yoga or meditation poses or hands outstretched. I have a lot of interesting ones that look like my example so if you are going to submit after Saturday 10/29, please only do so if you have a new idea! Thanks!

```html
<!DOCTYPE html>
<html lang="en">
<head>
<meta charset="utf-8">
<title>Lantern Road Ventures — Book Cover</title>
<link href="https://fonts.googleapis.com/css2?family=Allura&family=Tinos:wght@400&display=swap" rel="stylesheet">
<style>
  :root {
    --ink-black: #000000;
    --paper-white: #ffffff;
    --title-dark: #111111;
    --sky-top: #3f9fd8;
    --sky-mid: #8fcbec;
    --sky-glow: #e6f4fb;
    --ridge-dark: #0a0a0a;
    --portrait-green: #7f9a63;
    --portrait-rose: #d9546a;
  }
  * { margin: 0; padding: 0; box-sizing: border-box; }
  html, body {
    width: 1200px; height: 868px; overflow: hidden;
    background: var(--ink-black);
  }
  .cover {
    position: relative; width: 1200px; height: 868px;
    background: var(--ink-black);
    font-family: "Tinos", "Times New Roman", serif;
    color: var(--paper-white);
  }

  /* Back cover */
  .back { position: absolute; left: 0; top: 0; width: 584px; height: 868px; }
  .back-title { position: absolute; left: 0; top: 52px; width: 590px; text-align: center; }
  .back-title .script {
    display: block; font-family: "Allura", cursive; font-size: 64px; line-height: 1;
  }
  .back-title .caps {
    display: block; margin-top: -14px; font-size: 19px; letter-spacing: 0.22em;
  }
  .blurb {
    position: absolute; left: 62px; top: 178px; width: 462px;
    font-size: 12.6px; line-height: 19.6px; text-align: justify;
  }
  .blurb p { margin-bottom: 14px; }
  .blurb ol { list-style: none; margin-bottom: 14px; text-align: left; }
  .blurb li { padding-left: 14px; text-indent: -14px; }
  .author-photo {
    position: absolute; left: 62px; top: 538px; width: 122px; height: 152px;
    background: linear-gradient(180deg, var(--portrait-green) 0%, #a98a6e 55%, var(--portrait-rose) 100%);
  }
  .bio {
    position: absolute; left: 202px; top: 536px; width: 322px;
    font-size: 12.6px; line-height: 18.3px; text-align: justify;
  }

  /* Spine */
  .spine { position: absolute; left: 584px; top: 0; width: 40px; height: 868px; }
  .spine-text {
    position: absolute; left: 40px; top: 66px; width: 760px;
    transform-origin: 0 0; transform: rotate(90deg);
    white-space: nowrap; display: flex; align-items: baseline; gap: 6px;
  }
  .spine-text .script { font-family: "Allura", cursive; font-size: 30px; }
  .spine-text .caps { font-size: 21px; letter-spacing: 0.02em; }

  /* Front cover */
  .front { position: absolute; left: 624px; top: 0; width: 576px; height: 868px; overflow: hidden; }
  .front-scene {
    position: absolute; inset: 0;
    background:
      radial-gradient(ellipse 180px 160px at 52% 48%, var(--sky-glow) 0%, rgba(230,244,251,0) 100%),
      linear-gradient(180deg, var(--sky-top) 0%, var(--sky-mid) 35%, #bfe2f4 48%, #6d8ea3 58%, var(--ridge-dark) 66%, var(--ink-black) 100%);
  }
  .front-title { position: absolute; left: 0; top: 54px; width: 576px; text-align: center; }
  .front-title .script {
    display: block; font-family: "Allura", cursive; font-size: 104px; line-height: 1;
    color: var(--paper-white);
  }
  .front-title .caps {
    display: block; margin-top: -6px; font-size: 37px; letter-spacing: 0.3em;
    color: var(--title-dark);
  }
  .subtitle {
    position: absolute; left: 0; top: 557px; width: 566px; text-align: center;
    font-size: 20px; line-height: 45.5px;
  }
  .author {
    position: absolute; left: 0; top: 762px; width: 576px; text-align: center;
    font-size: 42px; letter-spacing: 0.12em;
  }
</style>
</head>
<body>
<div class="cover">

  <section class="back">
    <h2 class="back-title">
      <span class="script">Lantern Road</span>
      <span class="caps">VENTURES</span>
    </h2>
    <div class="blurb">
      <p>LANTERN ROAD VENTURES : Loose Pages of a Harbor Keeper is an honest account of a business owner’s experience attempting to navigate the start-up community while also pursuing spiritual growth. Author Mirela Dunbar defines a spiritual entrepreneur as “someone who runs an enterprise with the purpose of growing love rather than material gain.” This book discusses the three dimensions of Lantern Road Ventures:</p>
      <ol>
        <li>1. The business is an integral part of the founder’s spiritual journey.</li>
        <li>2. Employees working for the spiritual enterprise, whether they know it or not, encounter this company because it's part of their spiritual path.</li>
        <li>3. The business itself has a life force of its own and its purpose is to further the kingdom of heaven on earth.</li>
      </ol>
      <p>These three dimensions happen simultaneously and work together to produce the greatest possible result. However, this can feel confusing to a founder juggling these dimensions while also trying to manage and run a business. This is not a formulaic self-help book or roadmap. Rather, it is a compilation of personal reflections that often seem at odds with the traditional world of entrepreneurship.</p>
    </div>
    <div class="author-photo" role="img" aria-label="Portrait photo of the author outdoors"></div>
    <p class="bio">Mirela Dunbar founded Calveta with the vision of ushering in a life-long education system that shifts away from standardization to one that empowers people to live their purpose. In college, Mirela interned for Open Kettle, a women’s empowerment initiative where she recognized her passion for helping people find their voice. Mirela's 20-year journey has come full circle to empowering other female CEOs who are pursuing the path of Lantern Road Ventures.</p>
  </section>

  <section class="spine">
    <div class="spine-text">
      <span class="script">Lantern Road</span>
      <span class="caps">VENTURES AND MIRELA T. DUNBAR</span>
    </div>
  </section>

  <section class="front">
    <div class="front-scene" role="img" aria-label="Two hikers silhouetted on a mountain summit against a sunrise sky"></div>
    <h1 class="front-title">
      <span class="script">Lantern Road</span>
      <span class="caps">VENTURES</span>
    </h1>
    <p class="subtitle">LOOSE<br>PAGES OF<br>A HARBOR<br>KEEPER</p>
    <p class="author">MIRELA T. DUNBAR</p>
  </section>

</div>
</body>
</html>
```